Promotional Ad/Flyer - KVP Leasing

A division of our company, KVP Leasing (kvp-leasing.example) is celebrating its 1-year anniversary in September and we would like to run a promotion. I am looking to have a promotional ad/flyer made-up for email mailings and LinkedIn posts and possibly have on our site. Have plenty of product photos to share if needed, not a prerequisite to use our product in the ad but open to it. Can also be cool graphics as well. We want to capture the viewers attention with the 30 DAYS FREE! The message is simple:
We are celebrating our 1-Year Anniversary by offering a Special Peak-Season Promotion!

FREE RENTALS for 30 days with a minimum 30-Day rental!

Valid from Sep. 1 - Dec. 31 & while supplies last.

Please contact our sales department for more details.

Email: rfq@kvp-leasing.example
Phone: +1-555-284-3917

```html
<!DOCTYPE html>
<html lang="en">
<head>
<meta charset="utf-8">
<title>KVP Leasing – 1 Year Anniversary Promotion</title>
<link rel="stylesheet" href="https://fonts.googleapis.com/css2?family=Anton&family=Montserrat:wght@400;700;800&family=Poppins:wght@500;600&family=Tinos:ital,wght@0,700;1,700&display=swap">
<style>
  :root {
    --night: #120711;
    --night-deep: #0a0409;
    --gold: #e8b13a;
    --gold-light: #ffe08a;
    --gold-dark: #9a6414;
    --orange: #f26a0c;
    --ink: #161010;
    --white: #ffffff;
    --ribbon: #a3121a;
    --blue: #3557b8;
  }
  html, body { margin: 0; padding: 0; overflow: hidden; background: var(--night-deep); }
  .flyer {
    position: relative; width: 990px; height: 1200px; overflow: hidden;
    background:
      radial-gradient(ellipse 560px 340px at 495px 800px, rgba(232,177,58,.75), rgba(180,120,30,.35) 55%, rgba(18,7,17,0) 100%),
      linear-gradient(var(--night) 0%, #1a0c12 60%, #2a1810 100%);
    font-family: "Poppins", sans-serif; color: var(--white);
  }
  .bokeh {
    position: absolute; inset: 0;
    background: radial-gradient(ellipse 480px 260px at 495px 880px, rgba(255,210,110,.35), rgba(255,210,110,0) 100%);
  }
  .emblem { position: absolute; left: 0; top: 0; width: 990px; height: 470px; }
  .tagline-lead {
    position: absolute; top: 472px; width: 100%; margin: 0; text-align: center;
    font-family: "Tinos", serif; font-style: italic; font-weight: 700; font-size: 36px;
  }
  .tagline {
    position: absolute; top: 518px; width: 100%; margin: 0; text-align: center;
    font-family: "Tinos", serif; font-weight: 700; font-size: 53px;
    text-shadow: 2px 3px 4px rgba(0,0,0,.6);
  }
  .headline { position: absolute; left: 100px; top: 600px; width: 790px; height: 160px; }
  .offer-bar {
    position: absolute; left: 106px; top: 765px; width: 779px; height: 50px;
    background: var(--orange); display: flex; align-items: center; justify-content: center;
    font-weight: 600; font-size: 22px;
  }
  .offer-frame {
    position: absolute; left: 106px; top: 815px; width: 777px; height: 88px;
    border: 1px solid var(--orange); border-top: none;
  }
  .validity {
    position: absolute; left: 200px; top: 825px; width: 590px; height: 51px;
    background: var(--ink); display: flex; align-items: center; justify-content: center;
    font-family: "Montserrat", sans-serif; font-weight: 800; font-size: 37px;
  }
  .validity .dates { color: var(--orange); margin-left: 12px; }
  .supply {
    position: absolute; left: 334px; top: 884px; width: 322px; height: 38px;
    background: var(--ink); display: flex; align-items: center; justify-content: center;
    font-family: "Montserrat", sans-serif; font-weight: 800; font-size: 22px;
  }
  .brand {
    position: absolute; top: 956px; width: 100%; display: flex; justify-content: center; align-items: center; gap: 18px;
  }
  .brand-mark { width: 46px; height: 46px; border: 5px solid var(--white); box-sizing: border-box; }
  .brand-name { font-family: "Montserrat", sans-serif; font-weight: 800; font-size: 52px; letter-spacing: 1px; }
  .brand-sub {
    position: absolute; top: 1036px; left: 0; width: 100%; text-align: center;
    font-family: "Montserrat", sans-serif; font-size: 10px; letter-spacing: 1px; color: #d8d2cc; padding-left: 240px; box-sizing: border-box;
  }
  .contact-band { position: absolute; left: 0; top: 1094px; width: 990px; height: 106px; background: var(--blue); }
  .contact-bar {
    position: absolute; left: 106px; top: 1071px; width: 779px; height: 48px;
    background: var(--orange); display: flex; align-items: center; justify-content: center;
    font-family: "Montserrat", sans-serif; font-weight: 700; font-size: 19px; letter-spacing: .3px;
  }
  .contacts {
    position: absolute; top: 1130px; left: 0; width: 100%; display: flex; justify-content: center; align-items: center;
    font-weight: 600; font-size: 22px; gap: 18px;
  }
  .contacts .sep { width: 2px; height: 26px; background: var(--orange); }
  .contacts .item { display: flex; align-items: center; gap: 8px; }
  .contacts svg { width: 20px; height: 20px; }
</style>
</head>
<body>
<main class="flyer">
  <div class="bokeh" role="img" aria-label="Gold bokeh sparkle background"></div>

  <svg class="emblem" viewBox="0 0 990 470" aria-label="1 Year Anniversary emblem">
    <defs>
      <radialGradient id="wreath-glow" cx="50%" cy="50%" r="50%">
        <stop offset="0%" stop-color="#c88a2a" stop-opacity="0"/>
        <stop offset="70%" stop-color="#c88a2a" stop-opacity=".35"/>
        <stop offset="100%" stop-color="#c88a2a" stop-opacity="0"/>
      </radialGradient>
      <linearGradient id="ribbon-tone" x1="0" y1="0" x2="0" y2="1">
        <stop offset="0%" stop-color="#b5161f" stop-opacity=".85"/>
        <stop offset="100%" stop-color="#6e0c12" stop-opacity=".85"/>
      </linearGradient>
      <linearGradient id="gold-metal" x1="0" y1="0" x2="1" y2="0">
        <stop offset="0%" stop-color="#9a6414"/>
        <stop offset="45%" stop-color="#ffe08a"/>
        <stop offset="100%" stop-color="#b57a1f"/>
      </linearGradient>
      <path id="arc-title" d="M288 307 A207 207 0 0 1 702 307"/>
    </defs>
    <ellipse cx="495" cy="290" rx="200" ry="195" fill="url(#wreath-glow)" role="img" aria-label="Golden laurel wreath"/>
    <text font-family="Tinos, serif" font-weight="700" font-size="34" fill="#fff" letter-spacing="1">
      <textPath href="#arc-title" startOffset="50%" text-anchor="middle">WE ARE CELEBRATING OUR</textPath>
    </text>
    <text x="495" y="300" text-anchor="middle" font-family="Tinos, serif" font-weight="700" font-size="200" fill="url(#gold-metal)">1</text>
    <text x="495" y="354" text-anchor="middle" font-family="Tinos, serif" font-weight="700" font-size="40" fill="url(#gold-metal)">YEAR</text>
    <rect x="300" y="366" width="390" height="56" rx="8" fill="url(#ribbon-tone)" role="img" aria-label="Red anniversary ribbon"/>
    <text x="495" y="403" text-anchor="middle" font-family="Montserrat, sans-serif" font-size="26" fill="#f3c46a" letter-spacing="1">ANNIVERSARY</text>
  </svg>

  <p class="tagline-lead">by offering a</p>
  <p class="tagline">Special Peak-Season Promotion!</p>

  <svg class="headline" viewBox="0 0 790 160" aria-label="30 Days Free!">
    <defs>
      <linearGradient id="headline-gold" x1="0" y1="0" x2="0" y2="1">
        <stop offset="0%" stop-color="#f7d36a"/>
        <stop offset="50%" stop-color="#d9a32c"/>
        <stop offset="100%" stop-color="#b27b18"/>
      </linearGradient>
    </defs>
    <text x="14" y="150" font-family="Anton, sans-serif" font-size="164" textLength="770" lengthAdjust="spacingAndGlyphs" fill="#3a2410">30 DAYS FREE!</text>
    <text x="6" y="142" font-family="Anton, sans-serif" font-size="164" textLength="770" lengthAdjust="spacingAndGlyphs" fill="url(#headline-gold)" stroke="#fff" stroke-width="5" paint-order="stroke">30 DAYS FREE!</text>
  </svg>

  <div class="offer-bar">FREE RENTALS for 30 days with a minimum 30-Day rental!</div>
  <div class="offer-frame"></div>
  <div class="validity">VALID FROM <span class="dates">SEP. 1 - DEC. 31</span></div>
  <div class="supply">WHILE SUPPLIES LAST.</div>

  <div class="brand">
    <span class="brand-mark"></span>
    <span class="brand-name">KVP LEASING</span>
  </div>
  <div class="brand-sub">KVP-LEASING.EXAMPLE &nbsp;|&nbsp; BY NORVANE</div>

  <div class="contact-band"></div>
  <div class="contact-bar">PLEASE CONTACT OUR SALES DEPARTMENT FOR MORE DETAILS.</div>
  <div class="contacts">
    <span class="item">
      <svg viewBox="0 0 20 20" fill="none" stroke="#fff" stroke-width="1.5"><rect x="2" y="5" width="16" height="11"/><path d="M2 5 L10 11 L18 5"/></svg>
      rfq@kvp-leasing.example
    </span>
    <span class="sep"></span>
    <span class="item">
      <svg viewBox="0 0 20 20" fill="none" stroke="#fff" stroke-width="1.5"><circle cx="10" cy="10" r="8.5"/><path d="M7 5.5 L8.5 8 L7.5 9 Q8.5 11.5 11 12.5 L12 11.5 L14.5 13 L13.5 14.5 Q9 14.5 5.5 9 Q5.5 6.5 7 5.5 Z"/></svg>
      +1-555-284-3917
    </span>
    <span class="sep"></span>
    <span class="item">
      <svg viewBox="0 0 20 20" fill="none" stroke="#fff" stroke-width="1.5"><circle cx="10" cy="10" r="8.5"/><ellipse cx="10" cy="10" rx="3.5" ry="8.5"/><path d="M1.5 10 H18.5 M3 6 H17 M3 14 H17"/></svg>
      kvp-leasing.example
    </span>
  </div>
</main>
</body>
</html>
```